Website design for staffing/workforce solutions company - Harbor Crest Solutions

Create a launch-ready website
Harbor Crest Solutions also known as HCS. This is a company that specializes in Staffing/Work force solutions for Healthcare/IT/Logistics/Maintenance/Construction/Manufacturing/Industrial/General Labor. HCS works with government agencies/contracts also. Use the attached logo in the build of the website. Website should be clean, modern, engaging, innovative. Website needs to speak to the professional services industry.
Harbor Crest Solutions or HCS is a certified VOSB, SDVOSB, DBE and Minority-Owned Business.
The website needs to be compliant for government contracting.

Website needs to include the following--
Modern UI/UX Enhancements: A hero section with a strong call-to-action.
Government Contracting Compliance: Certification display and a Capability Statement download.
Advanced Careers Section: A dedicated job application portal.
Social Media & Lead Generation: Links to Workvine, Quillo, and Pagebloom.
Security & Performance: Optimized for SEO, fast loading, and mobile responsiveness.
1. Modern Design Upgrades
๐Ÿ”น Upgrade UI/UX for a Professional, Trustworthy Look
โœ… Full-width hero banner with a high-quality background image representing business, technology, and workforce solutions.
โœ… Animated elements (subtle transitions for smooth browsing experience).
โœ… Bold CTA buttons for easy navigation to key actions (e.g., โ€œGet Startedโ€ or โ€œRequest a Consultationโ€).
โœ… Dark-themed header with contrasting colors (professional & government-trustworthy).
โœ… New Homepage Hero Section Example:
"Your Trusted Partner in Workforce, IT, Maintenance & Logistics Solutions"
Button: "Discover Our Services"

2. Enhanced Government Contracting Section (Key for Compliance)
๐Ÿ“Œ Essential for securing contracts & building credibility
โœ… Capability Statement (Downloadable PDF)

Showcase key past contracts, company qualifications, and services in a downloadable format for government buyers.
โœ… Certifications Display (VOSB, SDVOSB, DBE, Minority-Owned Business)

Visual badge display to emphasize legitimacy for government contracts.
โœ… Procurement Readiness Details

NAICS Codes, DUNS Number, CAGE Code, and relevant KPR.example registration details.
โœ… Past Performance Showcase (Case Studies Section)

Highlight successful projects and government contracts.
โœ… Compliance & Security

Add SOC 2, HIPAA (for healthcare staffing), and ITAR compliance if applicable.
3. Advanced Job Search & Candidate Portal (For Staffing Services)
๐Ÿ“Œ To attract top talent for staffing contracts

โœ… Advanced Job Search Feature

Filters: Industry, location, job type (contract/full-time), salary range, and clearance level (for government jobs).
โœ… Candidate Login Portal

Applicants can upload resumes, track applications, and receive job alerts.
โœ… Employer Portal (For Businesses Hiring Through HCS)

A dedicated section for companies to submit staffing requests and view candidate matches.
4. Service-Specific Landing Pages (SEO & Engagement)
๐Ÿ“Œ Helps different industries find relevant services faster

๐Ÿ”น Dedicated Pages for Each Service:
โœ… Staffing & Workforce Solutions

Specialized sections for Healthcare, IT, Construction, Industrial, and General Labor staffing.
โœ… IT Services

List services like Cybersecurity, Cloud Solutions, and IT Consulting.
Showcase tech stack & certifications.
โœ… Logistics & Maintenance

Detail fleet management, supply chain services, and industrial maintenance.
โœ… Government Contracting Solutions

A streamlined page for government agencies.
5. Security & Compliance Upgrades (For Government Work)
๐Ÿ“Œ To ensure compliance & credibility in government contracting

โœ… SSL Certification (100% Required for Security)

Secure client and job applicant data.
โœ… ADA Compliance (Accessibility)

Ensure the website follows WCAG 2.1 accessibility standards for government clients.
โœ… GDPR & Data Protection Features

A privacy policy and terms of service to comply with data regulations.
6. Performance & Mobile Optimization
๐Ÿ“Œ To ensure fast loading & responsiveness

โœ… Mobile-Responsive Design

Optimized for mobile-friendly navigation since many users browse from phones.
โœ… Fast-Loading Pages

Optimize images & implement lazy loading for better site speed.
โœ… SEO-Optimized Pages

Improve search ranking on Findoro with:
Keyword-optimized content (e.g., โ€œGovernment Contracting Staffing Servicesโ€)
Schema markup for job listings
Blog/articles about staffing trends
7. Social Media & Lead Generation
๐Ÿ“Œ For brand credibility & client engagement

โœ… Workvine, Quillo, Pagebloom Integration

Display recent updates from Workvine (primary for B2B & government).
โœ… Lead Capture Forms

Forms for business inquiries, talent applications, and government RFPs.
โœ… Client & Candidate Testimonials
Showcase client success stories & employee experiences

Good websites to pull examples for inspiration/direction--
https://www.vlmn.example/
https://www.torvana.example/
https://brightmeridian.example/homepage/
https://www.valdorcheck.example/capability-statement

Industry/Entity Type

Staffing/Professional Services

Coding

Coded - Design and coding required

Number of Pages Required

5+ page

Requirements
Must have
• Website needs to include the following-- Modern UI/UX Enhancements: A hero section with a strong call-to-action. Government Contracting Compliance: Certification display and a Capability Statement download. Advanced Careers Section: A dedicated job application portal. Social Media & Lead Generation: Links to Workvine, Quillo, and Pagebloom. Security & Performance: Optimized for SEO, fast loading, and mobile responsiveness. 1. Modern Design Upgrades ๐Ÿ”น Upgrade UI/UX for a Professional, Trustworthy Look โœ… Full-width hero banner with a high-quality background image representing business, technology, and workforce solutions. โœ… Animated elements (subtle transitions for smooth browsing experience). โœ… Bold CTA buttons for easy navigation to key actions (e.g., โ€œGet Startedโ€ or โ€œRequest a Consultationโ€). โœ… Dark-themed header with contrasting colors (professional & government-trustworthy). โœ… New Homepage Hero Section Example: "Your Trusted Partner in Workforce, IT, & Logistics Solutions" Button: "Discover Our Services" 2. Enhanced Government Contracting Section (Key for Compliance) ๐Ÿ“Œ Essential for securing contracts & building credibility โœ… Capability Statement (Downloadable PDF) Showcase key past contracts, company qualifications, and services in a downloadable format for government buyers. โœ… Certifications Display (VOSB, SDVOSB, DBE, Minority-Owned Business) Visual badge display to emphasize legitimacy for government contracts. โœ… Procurement Readiness Details NAICS Codes, DUNS Number, CAGE Code, and relevant KPR.example registration details. โœ… Past Performance Showcase (Case Studies Section) Highlight successful projects and government contracts. โœ… Compliance & Security Add SOC 2, HIPAA (for healthcare staffing), and ITAR compliance if applicable. 3. Advanced Job Search & Candidate Portal (For Staffing Services) ๐Ÿ“Œ To attract top talent for staffing contracts โœ… Advanced Job Search Feature Filters: Industry, location, job type (contract/full-time), salary range, and clearance level (for government jobs). โœ… Candidate Login Portal Applicants can upload resumes, track applications, and receive job alerts. โœ… Employer Portal (For Businesses Hiring Through HCS) A dedicated section for companies to submit staffing requests and view candidate matches. 4. Service-Specific Landing Pages (SEO & Engagement) ๐Ÿ“Œ Helps different industries find relevant services faster ๐Ÿ”น Dedicated Pages for Each Service: โœ… Staffing & Workforce Solutions Specialized sections for Healthcare, IT, Construction, Industrial, and General Labor staffing. โœ… IT Services List services like Cybersecurity, Cloud Solutions, and IT Consulting. Showcase tech stack & certifications. โœ… Logistics & Maintenance Detail fleet management, supply chain services, and industrial maintenance. โœ… Government Contracting Solutions A streamlined page for government agencies. 5. Security & Compliance Upgrades (For Government Work) ๐Ÿ“Œ To ensure compliance & credibility in government contracting โœ… SSL Certification (100% Required for Security) Secure client and job applicant data. โœ… ADA Compliance (Accessibility) Ensure the website follows WCAG 2.1 accessibility standards for government clients. โœ… GDPR & Data Protection Features A privacy policy and terms of service to comply with data regulations. 6. Performance & Mobile Optimization ๐Ÿ“Œ To ensure fast loading & responsiveness โœ… Mobile-Responsive Design Optimized for mobile-friendly navigation since many users browse from phones. โœ… Fast-Loading Pages Optimize images & implement lazy loading for better site speed. โœ… SEO-Optimized Pages Improve search ranking on Findoro with: Keyword-optimized content (e.g., โ€œGovernment Contracting Staffing Servicesโ€) Schema markup for job listings Blog/articles about staffing trends 7. Social Media & Lead Generation ๐Ÿ“Œ For brand credibility & client engagement โœ… Workvine, Quillo, Pagebloom Integration Display recent updates from Workvine (primary for B2B & government). โœ… Lead Capture Forms Forms for business inquiries, talent applications, and government RFPs. โœ… Client & Candidate Testimonials Showcase client success stories & employee experiences Good websites to pull examples for inspiration/direction-- https://www.vlmn.example/ https://www.torvana.example/ https://brightmeridian.example/homepage/

```html
<!DOCTYPE html>
<html lang="en">
<head>
<meta charset="utf-8">
<title>Harbor Crest Solutions — Workforce, IT & Logistics</title>
<link rel="stylesheet" href="https://fonts.googleapis.com/css2?family=Montserrat:wght@400;500;600;700;800&display=swap">
<style>
:root{
  --red:#d0101b;
  --red-dark:#9e0a12;
  --ink:#141414;
  --black:#0b0b0b;
  --grey:#6b6b6b;
  --line:#dcdcdc;
  --paper:#ffffff;
  --soft:#f2f2f2;
}
*{box-sizing:border-box;margin:0;padding:0}
html,body{width:1200px;height:4608px;overflow:hidden}
body{font-family:"Montserrat",sans-serif;color:var(--ink);background:var(--paper);position:relative}
.abs{position:absolute}
.btn{display:inline-flex;align-items:center;gap:8px;background:var(--red);color:#fff;font-weight:700;font-size:13px;letter-spacing:.5px;padding:12px 22px;border-radius:3px;text-transform:uppercase}
.btn-outline{background:transparent;border:1px solid #fff}
.eyebrow{font-size:13px;font-weight:700;letter-spacing:2px;text-transform:uppercase}
.title{font-weight:800;text-transform:uppercase;line-height:1.1}
.title .hl{color:var(--red)}
.body-text{font-size:15px;line-height:1.6;color:var(--grey)}

/* Hero */
.hero{left:0;top:0;width:1200px;height:720px;background:linear-gradient(90deg,#0a0a0a 0%,#1a1a1a 45%,#3a3a3a 75%,#262626 100%)}
.hero-photo{left:560px;top:0;width:640px;height:720px;background:radial-gradient(ellipse at 55% 45%,#6a5a50 0%,#3d3632 40%,#1c1a19 80%)}
.hero-fade{left:0;top:0;width:1200px;height:720px;background:linear-gradient(90deg,rgba(10,10,10,.95) 30%,rgba(10,10,10,0) 65%)}
.site-nav{left:0;top:0;width:1200px;height:90px;display:flex;align-items:center;padding:0 120px}
.brand{color:#fff;font-weight:800;font-size:26px;letter-spacing:1px;display:flex;align-items:center;gap:10px}
.brand-dot{width:14px;height:14px;background:var(--red)}
.nav-links{margin-left:auto;display:flex;gap:34px;align-items:center}
.nav-links a{color:#fff;font-size:13px;font-weight:600;text-transform:uppercase;text-decoration:none}
.nav-links a.active{border-bottom:2px solid var(--red);padding-bottom:4px}
.hero-copy{left:120px;top:250px;width:480px;color:#fff}
.hero-copy h1{font-size:36px;font-weight:800;text-transform:uppercase;line-height:1.15}
.hero-copy h1 .hl{color:var(--red)}
.hero-copy p{font-size:14px;line-height:1.6;color:#cfcfcf;margin:22px 0 26px}

/* Government */
.gov{left:0;top:720px;width:1200px;height:780px;background:var(--paper)}
.gov-head{left:120px;top:80px;display:flex;gap:80px;align-items:center;width:960px}
.gov-head h2{font-size:32px;width:380px}
.gov-head p{width:480px}
.tabs{left:120px;top:212px;width:960px;display:flex;gap:18px}
.tab{flex:1;height:64px;border:1px solid var(--line);display:flex;align-items:center;justify-content:center;text-align:center;font-size:13px;font-weight:700;color:var(--ink);padding:0 12px;line-height:1.3}
.tab.active{background:var(--ink);color:#fff;border-color:var(--ink)}
.cards{left:120px;top:340px;width:960px;display:grid;grid-template-columns:repeat(3,1fr);gap:24px}
.cap-card{height:360px;border:1px solid var(--line);padding:34px 30px;box-shadow:0 4px 18px rgba(0,0,0,.06);position:relative}
.cap-icon{width:52px;height:52px;border-radius:50%;background:#fbe3e4;display:flex;align-items:center;justify-content:center;margin-bottom:18px}
.cap-card h3{font-size:19px;font-weight:800;text-transform:uppercase;line-height:1.15;margin-bottom:14px}
.cap-card h3 .hl{color:var(--red);display:block}
.cap-card p,.cap-card li{font-size:13px;line-height:1.7;color:var(--grey)}
.cap-card ul{list-style:none}
.cap-card li::before{content:"";display:inline-block;width:6px;height:6px;background:var(--red);margin-right:8px;vertical-align:middle}
.cap-card .btn{position:absolute;left:30px;bottom:32px;font-size:12px}

/* About */
.about{left:0;top:1500px;width:1200px;height:560px;background:linear-gradient(90deg,#ececec,#f7f7f7)}
.about-red{left:0;top:0;width:680px;height:560px}
.about-photo{left:120px;top:190px;width:380px;height:250px;background:linear-gradient(135deg,#c9b79c,#8a7f6e 55%,#5a5550)}
.about-copy{left:680px;top:110px;width:420px}
.about-copy .eyebrow{color:var(--ink);display:flex;align-items:center;gap:12px}
.about-copy .eyebrow::after{content:"";width:90px;height:1px;background:var(--red)}
.about-copy h2{font-size:38px;margin:6px 0 20px}
.about-copy p{font-size:16px;line-height:1.6;margin-bottom:18px}
.about-copy p.lead{color:var(--ink)}

/* Careers */
.careers{left:0;top:2060px;width:1200px;height:640px}
.center-head{width:1200px;left:0;text-align:center}
.center-head h2{font-size:40px;margin-top:6px}
.center-head p{margin-top:10px;font-size:16px;color:var(--ink)}
.jobs{left:140px;top:250px;width:940px;display:grid;grid-template-columns:repeat(3,1fr);gap:20px}
.job-card{height:260px;border:1px solid var(--line);box-shadow:0 4px 18px rgba(0,0,0,.07);padding:36px 30px}
.tag{display:inline-block;background:#fbe3e4;color:var(--red);font-size:10px;font-weight:700;padding:4px 10px;text-transform:uppercase;letter-spacing:.5px}
.job-card h3{font-size:20px;font-weight:700;margin:14px 0 8px}
.job-card p{font-size:13px;line-height:1.5;color:var(--ink);margin-bottom:20px}
.job-card .btn{font-size:11px;padding:9px 16px}
.dots{left:520px;top:590px;display:flex;gap:12px}
.dots span{width:40px;height:3px;background:#ccc}
.dots span.on{background:var(--ink)}

/* Testimonials */
.testi{left:0;top:2700px;width:1200px;height:540px;background:linear-gradient(180deg,#0b0b0b,#1e1e1e 60%,#111)}
.testi-head{left:140px;top:90px;color:#fff}
.testi-head h2{font-size:40px;margin-top:4px}
.quotes{left:140px;top:190px;width:940px;display:grid;grid-template-columns:1fr 1fr;gap:50px}
.quote{height:290px;border:1px solid var(--red-dark);padding:30px 40px;color:#fff;position:relative}
.quote .mark{font-size:80px;font-weight:800;line-height:.7;color:#fff;position:absolute;left:40px;top:-20px;background:#141414;padding:0 8px}
.quote p{font-size:14px;line-height:1.7;color:#bdbdbd;margin-top:40px}
.quote h4{font-size:18px;font-weight:500;margin-top:20px}
.stars{color:#fff;font-size:13px;letter-spacing:3px;margin-top:4px}

/* Blogs */
.blogs{left:0;top:3240px;width:1200px;height:740px;background:linear-gradient(180deg,#ededed,#fff 40%)}
.blog-main{left:140px;top:190px;width:470px;height:490px;background:linear-gradient(160deg,#8d735c,#4b3a2e 55%,#1b1512)}
.blog-main-copy{left:170px;top:540px;width:400px;color:#fff}
.date{display:inline-block;background:var(--red);color:#fff;font-size:10px;font-weight:700;padding:4px 10px}
.blog-main-copy h3{font-size:22px;font-weight:700;margin:12px 0 6px}
.blog-main-copy p{font-size:12px;line-height:1.5;color:#ddd}
.blog-thumb{left:640px;width:230px;height:220px}
.blog-card{left:850px;width:230px;height:170px;background:#fff;border:1px solid var(--line);box-shadow:0 4px 18px rgba(0,0,0,.08);padding:22px 20px}
.blog-card h3{font-size:18px;font-weight:700;margin:10px 0 6px}
.blog-card p{font-size:12px;line-height:1.5;color:var(--grey)}

/* CTA */
.cta{left:136px;top:3990px;width:954px;height:190px;background:linear-gradient(90deg,#b80d17,var(--red) 55%,#8e0a12);display:flex;align-items:center;padding:0 80px;color:#fff}
.cta h2{font-size:32px;font-weight:800;text-transform:uppercase;margin:6px 0}
.cta p{font-size:13px;line-height:1.5;color:#f3c9cb;width:360px}
.cta .btn{margin-left:auto}

/* Footer */
.footer{left:0;top:4180px;width:1200px;height:428px;background:var(--black);color:#fff}
.f-brand{left:140px;top:60px}
.f-brand .brand{font-size:28px}
.f-brand .tagline{font-size:10px;letter-spacing:1px;color:#aaa;margin-top:6px;text-transform:uppercase}
.socials{display:flex;gap:14px;margin-top:34px}
.socials span{display:flex;align-items:center;gap:6px;font-size:12px;color:#ddd}
.socials span::before{content:"";width:10px;height:10px;border-radius:50%;background:var(--red)}
.f-col{top:60px}
.f-col h4{font-size:16px;font-weight:700;text-transform:uppercase;border-left:3px solid var(--red);padding-left:10px;margin-bottom:18px}
.f-col li{list-style:none;font-size:13px;color:#c9c9c9;line-height:2;padding-left:13px}
.f-rule{left:140px;top:348px;width:920px;height:1px;background:#2c2c2c}
.copyright{left:0;top:370px;width:1200px;text-align:center;font-size:12px;color:#aaa}
</style>
</head>
<body>

<header class="abs hero">
  <div class="abs hero-photo" role="img" aria-label="Professional woman holding a tablet in a modern office"></div>
  <div class="abs hero-fade"></div>
  <nav class="abs site-nav">
    <div class="brand"><span class="brand-dot"></span>HARBOR CREST</div>
    <div class="nav-links">
      <a class="active">Home</a><a>Government Contracting</a><a>Jobs</a><a>Services</a><a>Contact Us</a>
      <span class="btn">Get Started ›</span>
    </div>
  </nav>
  <div class="abs hero-copy">
    <h1><span class="hl">Your Trusted Partner</span><br>in Workforce, IT, &amp;<br>Logistics Solutions</h1>
    <p>Lorem ipsum dolor sit amet, consectetur adipiscing elit, sed do eiusmod tempor incididunt ut labore et dolore.</p>
    <span class="btn">Discover Our Services ›</span>
  </div>
</header>

<section class="abs gov">
  <div class="abs gov-head">
    <h2 class="title"><span class="hl">Government</span><br>Contracting</h2>
    <p class="body-text">Lorem ipsum dolor sit amet, consectetur adipiscing elit, sed do eiusmod tempor incididunt ut labore et dolore</p>
  </div>
  <div class="abs tabs">
    <div class="tab active">Capability Statement</div>
    <div class="tab">Certifications Display</div>
    <div class="tab">Procurement Readiness Details</div>
    <div class="tab">Past Performance Showcase</div>
    <div class="tab">Compliance &amp; Security</div>
  </div>
  <div class="abs cards">
    <article class="cap-card">
      <div class="cap-icon"><svg width="24" height="24" viewBox="0 0 24 24" fill="none" stroke="#d0101b" stroke-width="2"><rect x="5" y="3" width="14" height="18" rx="1"/><path d="M8 8h8M8 12h8M8 16h5"/></svg></div>
      <h3><span class="hl">Key Past</span>Contracts</h3>
      <p>Lorem ipsum dolor sit amet, consectetur adipiscing elit, sed do eiusmod tempor incididunt ut labore et dolore magna</p>
      <span class="btn">Download PDF ⤓</span>
    </article>
    <article class="cap-card">
      <div class="cap-icon"><svg width="24" height="24" viewBox="0 0 24 24" fill="none" stroke="#d0101b" stroke-width="2"><rect x="5" y="3" width="14" height="18" rx="1"/><path d="M8 9l2 2 4-4M8 15h8"/></svg></div>
      <h3>Company<br>Qualifications</h3>
      <ul><li>Lorem ipsum dolor sit amet</li><li>Consectetur adipiscing</li><li>Elit sed do eiusmod</li></ul>
      <span class="btn">Download PDF ⤓</span>
    </article>
    <article class="cap-card">
      <div class="cap-icon"><svg width="24" height="24" viewBox="0 0 24 24" fill="none" stroke="#d0101b" stroke-width="2"><circle cx="12" cy="8" r="4"/><path d="M4 21c0-4 4-6 8-6s8 2 8 6"/></svg></div>
      <h3><span class="hl" style="display:inline">Services</span> Provide</h3>
      <ul><li>Staffing &amp; Workforce Solutions</li><li>IT Services</li><li>Logistics &amp; Maintenance</li><li>Government Contracting Solutions</li></ul>
      <span class="btn">Download PDF ⤓</span>
    </article>
  </div>
</section>

<section class="abs about">
  <svg class="abs about-red" width="680" height="560" viewBox="0 0 680 560"><polygon points="0,0 280,0 160,560 0,560" fill="#d0101b"/><polygon points="280,0 360,0 240,560 160,560" fill="#b00d16"/></svg>
  <div class="abs about-photo" role="img" aria-label="Team of colleagues collaborating around a whiteboard"></div>
  <div class="abs about-copy">
    <div class="eyebrow">Who we are</div>
    <h2 class="title"><span class="hl">About</span> Harbor Crest</h2>
    <p class="lead">Lorem ipsum dolor sit amet, consectetur adipiscing elit, sed do eiusmod tempor incididunt ut labore.</p>
    <p class="body-text">Aebore et dolore magna aliqua. Quis ipsum suspendisse ultrices gravida. Risus commodo viverra maecenas accumsan lacus vel facilisis.</p>
    <span class="btn">Get Started ›</span>
  </div>
</section>

<section class="abs careers">
  <svg class="abs" style="left:598px;top:0" width="6" height="80" viewBox="0 0 6 80"><line x1="3" y1="0" x2="3" y2="72" stroke="#d0101b" stroke-width="1"/><circle cx="3" cy="75" r="3" fill="#d0101b"/></svg>
  <div class="abs center-head" style="top:110px">
    <div class="eyebrow">Featured jobs</div>
    <h2 class="title"><span class="hl">Advanced</span> Careers</h2>
    <p>Lorem ipsum dolor sit amet consectetur adipiscing elit, sed do eius</p>
  </div>
  <div class="abs jobs">
    <article class="job-card"><span class="tag">Healthcare</span><h3>Job Offer Heading</h3><p>Lorem ipsum dolor sit amet, consectetur adipiscing elit, sed do eiusmod temps</p><span class="btn">Apply Now ›</span></article>
    <article class="job-card"><span class="tag">IT Services</span><h3>Job Offer Heading</h3><p>Lorem ipsum dolor sit amet, consectetur adipiscing elit, sed do eiusmod temps</p><span class="btn">Apply Now ›</span></article>
    <article class="job-card"><span class="tag">Construction</span><h3>Job Offer Heading</h3><p>Lorem ipsum dolor sit amet, consectetur adipiscing elit, sed do eiusmod temps</p><span class="btn">Apply Now ›</span></article>
  </div>
  <div class="abs dots"><span class="on"></span><span></span><span></span></div>
</section>

<section class="abs testi">
  <div class="abs testi-head">
    <div class="eyebrow">Testimonials</div>
    <h2 class="title"><span class="hl">What People</span> Are Saying</h2>
  </div>
  <div class="abs quotes">
    <blockquote class="quote"><span class="mark">“</span><p>Lorem ipsum dolor sit amet, consectetur adipiscing elit, sed do eiusmod tempor incididunt ut labore et dolore magna aliqua. Quis ipsum suspendisse ultrices gravida. Risus commodo viverra maecenas accumsan lacus vel facilisis.</p><h4>John Smith</h4><div class="stars">★★★★★</div></blockquote>
    <blockquote class="quote"><span class="mark">“</span><p>Lorem ipsum dolor sit amet, consectetur adipiscing elit, sed do eiusmod tempor incididunt ut labore et dolore magna aliqua. Quis ipsum suspendisse ultrices gravida. Risus commodo viverra maecenas accumsan lacus vel facilisis.</p><h4>John Smith</h4><div class="stars">★★★★★</div></blockquote>
  </div>
</section>

<section class="abs blogs">
  <div class="abs center-head" style="top:60px">
    <div class="eyebrow">Resources</div>
    <h2 class="title"><span class="hl">Latest</span> Blogs</h2>
  </div>
  <div class="abs blog-main" role="img" aria-label="Colleagues reviewing work together at a table"></div>
  <div class="abs blog-main-copy"><span class="date">APR 02, 2025</span><h3>Blog Heading goes here</h3><p>Lorem ipsum dolor sit amet, consectetur adipiscing elit, sed do eiusmod tempor.</p></div>
  <div class="abs blog-thumb" style="top:190px;background:linear-gradient(135deg,#b9a897,#6f625a)" role="img" aria-label="Business team discussing documents"></div>
  <article class="abs blog-card" style="top:215px"><span class="date">APR 02, 2025</span><h3>Blog Heading here</h3><p>Lorem ipsum dolor sit amet, consectetur adipiscing elit.</p></article>
  <div class="abs blog-thumb" style="top:460px;background:linear-gradient(135deg,#c9b15a,#5d6470)" role="img" aria-label="Construction workers in safety vests on site"></div>
  <article class="abs blog-card" style="top:485px"><span class="date">APR 02, 2025</span><h3>Blog Heading here</h3><p>Lorem ipsum dolor sit amet, consectetur adipiscing elit.</p></article>
</section>

<footer class="abs footer">
  <div class="abs f-brand">
    <div class="brand"><span class="brand-dot"></span>HARBOR CREST</div>
    <div class="tagline">Partnering for your business success</div>
    <div class="socials"><span>Pagebloom</span><span>Quillo</span><span>Workvine</span></div>
  </div>
  <div class="abs f-col" style="left:440px"><h4>Navigation</h4><ul><li>Home</li><li>Government contracting</li><li>Jobs</li><li>Services</li><li>Contact Us</li></ul></div>
  <div class="abs f-col" style="left:670px"><h4>Services</h4><ul><li>Staffing &amp; Workforce Solutions</li><li>IT Services</li><li>Logistics &amp; Maintenance</li><li>Government Contracting</li></ul></div>
  <div class="abs f-col" style="left:930px"><h4>Resources</h4><ul><li>Blogs</li><li>Testimonials</li><li>Terms of Use</li><li>Privacy Policy</li><li>Sitemap</li></ul></div>
  <div class="abs f-rule"></div>
  <div class="abs copyright">Copyright © 2025 Harbor Crest. All Right Reserved</div>
</footer>

<section class="abs cta">
  <div>
    <div class="eyebrow">Get Started</div>
    <h2>Discover Our Services</h2>
    <p>Lorem ipsum dolor sit amet, consectetur adipiscing elit, sed do eiusmod tempor incididunt ut labore et dolore.</p>
  </div>
  <span class="btn btn-outline">Get Started ›</span>
</section>

</body>
</html>
```